Business card design for Tolbrin Waste

I would like double-sided business cards for myself and my partner that includes our logo and the existing colour scheme. We provide waste and environmental services to customers in the motor-vehicle and engineering industries.

```html
<!DOCTYPE html>
<html lang="en">
<head>
<meta charset="utf-8">
<title>Tolbrin Waste – Business Card</title>
<link rel="stylesheet" href="https://fonts.googleapis.com/css2?family=Source+Sans+3:wght@400;600;700&display=swap">
<style>
  :root {
    --backdrop: #3b312d;
    --card-white: #f7f7f5;
    --card-dark: #3f3f3f;
    --ink: #333333;
    --ink-soft: #555555;
    --brand-green: #7cc242;
    --rule: #c9c9c9;
    --white: #ffffff;
  }
  * { box-sizing: border-box; margin: 0; padding: 0; }
  html, body {
    width: 1200px;
    height: 844px;
    overflow: hidden;
    background: var(--backdrop);
    font-family: "Source Sans 3", "Myriad Pro", sans-serif;
  }
  .canvas {
    position: relative;
    width: 1200px;
    height: 844px;
    display: flex;
    align-items: center;
    justify-content: center;
    gap: 40px;
  }
  .card {
    position: relative;
    width: 525px;
    height: 300px;
    border-radius: 3px;
    box-shadow: 0 10px 24px rgba(0,0,0,0.35);
    overflow: hidden;
  }

  /* Front */
  .card-front { background: var(--card-white); color: var(--ink); }
  .brand {
    position: absolute;
    top: 38px;
    right: 40px;
    display: flex;
    align-items: center;
    gap: 12px;
  }
  .brand-dot {
    width: 44px;
    height: 44px;
    border-radius: 50%;
    background: var(--brand-green);
  }
  .brand-name {
    font-weight: 700;
    font-size: 34px;
    letter-spacing: 1px;
    color: var(--ink);
    text-transform: uppercase;
  }
  .top-rule {
    position: absolute;
    top: 108px;
    left: 160px;
    right: 40px;
    border-top: 1px solid var(--rule);
  }
  .details {
    position: absolute;
    left: 40px;
    right: 40px;
    top: 132px;
  }
  .person-name {
    font-weight: 700;
    font-size: 20px;
    color: var(--brand-green);
    text-transform: uppercase;
    line-height: 1.1;
  }
  .person-role {
    font-size: 15px;
    color: var(--ink);
    margin-bottom: 12px;
  }
  .address { font-size: 15px; color: var(--ink); }
  .contact-rule {
    border-top: 1px solid var(--rule);
    margin: 12px 0 10px;
    width: 60%;
  }
  .contact-line { font-size: 14px; color: var(--ink); line-height: 1.55; }
  .contact-line .label { color: var(--brand-green); }
  .contact-line .item { margin-right: 10px; }
  .web { color: var(--brand-green); }

  /* Back */
  .card-back {
    background: var(--card-dark);
    display: flex;
    align-items: center;
    justify-content: center;
  }
  .back-brand {
    text-align: center;
    color: var(--white);
    text-transform: uppercase;
    font-weight: 700;
  }
  .back-brand .word-main { font-size: 58px; letter-spacing: 2px; line-height: 1; }
  .back-brand .word-sub { font-size: 58px; letter-spacing: 2px; line-height: 1; }
</style>
</head>
<body>
  <main class="canvas">
    <section class="card card-front" aria-label="Business card front">
      <div class="brand">
        <span class="brand-dot"></span>
        <span class="brand-name">Tolbrin Waste</span>
      </div>
      <div class="top-rule"></div>
      <div class="details">
        <p class="person-name">Marcus Hale</p>
        <p class="person-role">Managing Director</p>
        <p class="address">12345, Address Goes Here Country Name, 123456.</p>
        <div class="contact-rule"></div>
        <p class="contact-line">
          <span class="item"><span class="label">T:</span>(044) 123 456 789</span>
          <span class="item"><span class="label">F:</span>(044) 123456789</span>
          <span class="item"><span class="label">M:</span>(044)123456789</span>
        </p>
        <p class="contact-line">
          <span class="item"><span class="label">E:</span>info@youremail.com</span>
          <span class="web">www.yourweb.com</span>
        </p>
      </div>
    </section>

    <section class="card card-back" aria-label="Business card back">
      <div class="back-brand">
        <p class="word-main">Tolbrin</p>
        <p class="word-sub">Waste</p>
      </div>
    </section>
  </main>
</body>
</html>
```